Vistalune Web Design Project

We need a new web site for our company. Vistalune provides a range of location intelligence and marketing services to assist clients in improving their performance. On the location intelligence side we're the local partner for Orbix Terra (Charts and Globe) in South Africa, we're the local reseller and can assist company with the implementation and customization - we'll shortly receive the Orbix partner logo that should also be displayed on the Homepage. On the marketing side, we provide a range of marketing services for example Tenders, Event Management and Copy writing. The company is a blend between a mapping and marketing services company. You can have a look at the existing site at www.vistalune.co.za
Updates

Dear designers, the budget for my project has been increased to $700. Looking forward to receiving your designs. Kind regards Henrik

Dear designers - many thanks for all the great designs received to date. We'll provide feedback shortly. Kind regards Vistalune

Target Market(s)

Our target market is public and private organisations, and online customers (those with a web presence) primarily in South Africa

Industry/Entity Type

Marketing

Requirements
Must have
• I have uploaded the latest text and suggested pages at this stage. Important is that it should be easy to edit the pages in an HTML editor, e.g. Pagecraft. I suspect that the navigation will be expanded later e.g. careers, success stories - so it should be easy for me add new sections to the navigation later on. I have also uploaded the different Vistalune logo designs. Please include links on the Homepage for Terms and Conditions and PAIA - see www.vistalune.co.za - also the Copyright Note at the bottom of every page
Nice to have
• Although we're targeting corporates and government, and online customers, the site should be fresh and easy to navigate. I like the use of photographs on sites and make them look more interesting than simply text. Although we're also providing marketing services, the location intelligence (mapping) and Orbix Charts/Globe aspect are perhaps the most important part of the website.

```html
<!DOCTYPE html>
<html lang="en">
<head>
<meta charset="utf-8">
<title>Vistalune – Location Intelligence &amp; Marketing</title>
<link href="https://fonts.googleapis.com/css2?family=Ubuntu:wght@300;400;500&family=PT+Sans+Narrow:wght@400;700&family=Open+Sans:wght@400;600&family=PT+Serif:wght@400;700&display=swap" rel="stylesheet">
<style>
:root{
  --red:#d81e27;
  --red-dark:#b5151d;
  --cream:#f3eee4;
  --ink:#333;
  --muted:#666;
  --slate:#3f4549;
  --green:#6cb52d;
  --gold:#ffd200;
  --white:#fff;
  --line:#e3e0da;
}
*{margin:0;padding:0;box-sizing:border-box}
html,body{width:1091px;height:1200px;overflow:hidden}
body{position:relative;background:var(--cream);font-family:"Open Sans",Arial,sans-serif;color:var(--ink)}
.abs{position:absolute}
.top-band{left:0;top:0;width:1091px;height:16px;background:var(--red);border-bottom:2px dashed #f0a0a4}
.page{left:99px;top:120px;width:891px;height:1038px;background:var(--white)}
.ribbon{left:126px;top:0;width:132px;height:177px;z-index:5}
.brand{left:134px;top:44px;width:118px;z-index:6;text-align:center;font-family:"Ubuntu",sans-serif;font-weight:500;font-size:24px;color:var(--red)}
.brand-dot{display:block;width:34px;height:34px;margin:0 auto 4px;border-radius:50%;background:var(--slate)}
.callout{right:100px;top:22px;font-family:"PT Sans Narrow",sans-serif;font-size:18px;color:var(--ink);white-space:nowrap}
.callout b{color:var(--red);font-weight:400}
.follow{right:100px;top:52px;font-family:"PT Sans Narrow",sans-serif;font-size:14px;display:flex;align-items:center;gap:4px}
.follow span{margin-right:3px}
.sq{display:inline-block;width:19px;height:19px;border-radius:2px}
.nav{left:99px;top:76px;width:891px;height:44px;background:linear-gradient(#e3242d,var(--red-dark));border-radius:6px 6px 0 0}
.nav ul{list-style:none;display:flex;justify-content:space-between;position:absolute;left:174px;top:14px;width:693px}
.nav li{font-family:"PT Sans Narrow",sans-serif;font-size:14px;line-height:16px;color:var(--white);text-transform:uppercase;white-space:nowrap}
.nav li.current{color:var(--gold)}
.hero{left:99px;top:120px;width:891px;height:339px;background:linear-gradient(90deg,#eef1f2 0%,#dfe6e6 35%,#a7b29a 60%,#6d7f5c 100%)}
.hero-copy{left:118px;top:240px;width:430px;font-family:"Ubuntu",sans-serif;font-weight:300;font-size:23px;line-height:33px;color:#444}
.hero-copy b{color:var(--red);font-weight:500}
.discover{left:118px;top:384px;width:101px;height:25px;background:linear-gradient(#8fd14a,var(--green));border-radius:3px;color:var(--white);font-family:"PT Sans Narrow",sans-serif;font-size:15px;line-height:25px;padding-left:8px}
.discover svg{position:absolute;right:8px;top:7px}
.welcome h1{font-family:"Ubuntu",sans-serif;font-weight:300;font-size:28px;color:#444;white-space:nowrap}
.welcome h1 b{color:var(--red);font-weight:400;font-size:32px}
.welcome{left:111px;top:474px;width:520px}
.welcome p{font-size:10.5px;line-height:16.4px;color:var(--muted);margin-top:6px}
.welcome p+p{margin-top:16px}
.testimonial{left:655px;top:466px;width:295px;height:158px;background:#f7f6f3;padding:10px 20px}
.testimonial h2{font-family:"Ubuntu",sans-serif;font-weight:400;font-size:22px;line-height:28px;color:#333;padding-bottom:8px;border-bottom:1px solid var(--line)}
.testimonial p{font-family:"Ubuntu",sans-serif;font-size:12.5px;line-height:16.4px;margin-top:10px}
.testimonial .who{font-size:10px;line-height:14px;margin-top:14px}
.testimonial .url{font-size:10px;line-height:14px;color:var(--green);margin-top:2px}
.service{top:655px;width:205px}
.service h3{font-family:"PT Sans Narrow",sans-serif;font-weight:400;font-size:18px;line-height:22px;color:var(--slate);text-transform:uppercase;height:29px;white-space:nowrap}
.service .photo{width:201px;height:80px}
.service p{font-family:"Ubuntu",sans-serif;font-weight:300;font-size:12px;line-height:16.4px;color:#333;margin:11px 0 0 10px;width:188px}
.footer-col{top:940px}
.footer-col h4{font-family:"PT Serif",serif;font-weight:400;font-size:13px;color:#555;padding-bottom:12px;border-bottom:1px solid var(--line)}
.footer-col p{font-size:10.3px;line-height:16.4px;color:#666;letter-spacing:.3px;margin-top:12px}
.footer-col ul{list-style:none;margin-top:12px}
.offer li{font-size:9.5px;color:#777;line-height:21.8px;white-space:nowrap}
.contact li{font-family:"PT Sans Narrow",sans-serif;font-size:12px;color:#333;line-height:27px;white-space:nowrap}
.contact li a{font-family:"Open Sans",sans-serif;font-size:10.5px;color:#c87a14}
.inquiry{left:778px;top:1065px;width:160px;height:27px}
.inquiry span{position:absolute;left:12px;top:7px;font-family:"PT Serif",serif;font-weight:700;font-size:11px;color:var(--white);text-transform:uppercase;white-space:nowrap}
.foot-social{left:782px;top:1120px;display:flex;gap:13px}
.foot-social .sq{width:25px;height:25px;background:#5a6165}
.bottom-bar{left:0;top:1158px;width:1091px;height:42px;background:var(--slate);color:#e6e6e6;font-size:11px}
.bottom-bar .copy{position:absolute;left:118px;top:14px}
.bottom-bar .legal{position:absolute;right:120px;top:13px}
</style>
</head>
<body>
<div class="abs top-band"></div>
<div class="abs page"></div>

<svg class="abs ribbon" viewBox="0 0 132 177" aria-hidden="true">
  <path d="M0 0H132V172L66 112L0 172Z" fill="#fbfbfa" stroke="#e4e2de"/>
</svg>
<div class="abs brand"><span class="brand-dot"></span>Vistalune</div>

<div class="abs callout"><b>Call Now!</b> +27 21 555 0192 - <b>Email:</b> info@vistalune.co.za</div>
<div class="abs follow"><span>Follow Us On:</span><i class="sq" style="background:#e8892a"></i><i class="sq" style="background:#3b5b9a"></i><i class="sq" style="background:#35a8dd"></i><i class="sq" style="background:#1b7eb8"></i></div>

<nav class="abs nav"><ul>
  <li class="current">Home</li><li>About Us</li><li>Services</li><li>Products</li><li>Map Office</li><li>Tender Office</li><li>Sales Office</li><li>Content Office</li><li>Event Office</li>
</ul></nav>

<div class="abs hero" role="img" aria-label="Photo of two hikers with backpacks walking along a green coastal hillside"></div>
<div class="abs hero-copy"><b>Vistalune</b> provides a range of location intelligence and marketing services and products to assist clients in improving their performance.</div>
<div class="abs discover">DISCOVER<svg width="10" height="11" viewBox="0 0 10 11"><path d="M2 1l5 4.5L2 10" stroke="#2a4d10" stroke-width="2.4" fill="none"/></svg></div>

<section class="abs welcome">
  <h1>Welcome to <b>Vistalune</b></h1>
  <p>Vistalune provides a range of location intelligence and marketing services and products to assist clients in improving their performance. We enjoy challenging projects that stretch the imagination and encourage out of the box thinking.</p>
  <p>We have extensive experience in providing world-class service to private and public organisations, locally as well as internationally and we strive to build long-term lasting relationships with our clients.</p>
</section>

<aside class="abs testimonial">
  <h2>Our Client Says...</h2>
  <p>These guys did really very excellent job, I must recommend them to all. Vistalune team is honest and healthy in work progress.</p>
  <p class="who">Tariq Noorani - Co-Founder [ UAE ]</p>
  <p class="url">www.corvanta-systems.com</p>
</aside>

<div class="abs service" style="left:105px">
  <h3>Marketing Services</h3>
  <div class="photo" role="img" aria-label="Photo of a receptionist at a desk in a bright office" style="background:linear-gradient(90deg,#5c7a48,#c9d3d8 40%,#e9eef2)"></div>
  <p>Vistalune provides a complete turnkey solution to companies participating in government and parastatal tenders. Tailor-made tender services are also offered for companies requiring assistance</p>
</div>
<div class="abs service" style="left:330px">
  <h3>Consulting</h3>
  <div class="photo" role="img" aria-label="Photo of a business team in suits" style="background:linear-gradient(90deg,#e8e8e8,#b6b8bb 55%,#3a3c42)"></div>
  <p>Vistalune has extensive experience in managing large complex projects, from conceptualisation to implementation and support.</p>
</div>
<div class="abs service" style="left:560px">
  <h3>Software Development</h3>
  <div class="photo" role="img" aria-label="Blue digital world map graphic with the word innovation" style="background:linear-gradient(135deg,#0a3c8a,#1f7fd6 60%,#0b4aa0)"></div>
  <p>Vistalune development team is well versed in deploying various system development life-cycle (SDLC) methodologies, including Waterfall, V-model, Spiral, Scrum and Rapid Application Development (RAD).</p>
</div>
<div class="abs service" style="left:786px">
  <h3>Orbix Charts for Business</h3>
  <div class="photo" role="img" aria-label="Illustration of a folded map with a pin and a compass" style="background:linear-gradient(135deg,#f4f1ea,#c9cdd0 55%,#4a5560)"></div>
  <p>Vistalune is the local partner for Orbix Terra products in South Africa. Contact us for any technical, commercial or legal queries regarding these products.</p>
</div>

<section class="abs footer-col" style="left:110px;width:425px">
  <h4>ABOUT US</h4>
  <p>Vistalune provides a range of location intelligence and marketing services and products to assist clients in improving their performance. We enjoy challenging projects that stretch the imagination and encourage out of the box thinking. We have extensive experience in providing world-class service to private and public organisations, locally as well as internationally and we strive to build long-term lasting relationships with our clients.</p>
</section>
<section class="abs footer-col offer" style="left:556px;width:200px">
  <h4 style="border:0">WHAT WE OFFER</h4>
  <ul>
    <li>+ Developing a sales strategy</li>
    <li>+ Identifying the value proposition</li>
    <li>+ Focusing on the target market</li>
    <li>+ Analysing products/services</li>
    <li>+ Assessing operational readiness</li>
    <li>+ Creating a product/brand strategy</li>
  </ul>
</section>
<section class="abs footer-col contact" style="left:778px;width:205px">
  <h4>CONTACT US</h4>
  <ul>
    <li>+&nbsp; Call Now! +27 21 555 0192</li>
    <li>+&nbsp; Email: info@vistalune.co.za</li>
    <li>+&nbsp; <a>Show legal info</a></li>
  </ul>
</section>
<svg class="abs inquiry" viewBox="0 0 160 27" aria-hidden="true"><path d="M3 0H147L160 13.5L147 27H3Q0 27 0 24V3Q0 0 3 0Z" fill="#e5585e"/></svg>
<div class="abs inquiry"><span>Design Inquiry Form</span></div>
<div class="abs" style="left:778px;top:1102px;width:210px;border-top:1px solid var(--line)"></div>
<div class="abs foot-social"><i class="sq"></i><i class="sq"></i><i class="sq"></i><i class="sq"></i></div>

<footer class="abs bottom-bar">
  <span class="copy">© Copyright 2012 Vistalune. All Rights Reserved.</span>
  <span class="legal">Terms and Conditions &nbsp;|&nbsp; Privacy Policy</span>
</footer>
</body>
</html>
```